Crossing the Amber Delta: Strength-Rooted Team Renewal

Target is Meridian 100 managers in Information Technology. I've led Agile transformations for over 60 organizations since 2005. One of these organizations is using my collateral internally so I'm branding and copyrighting key concepts. I've attached a rough idea of what I'm looking for. My website is www.strengthrootedteam.example.

```html
<!DOCTYPE html>
<html lang="en">
<head>
<meta charset="utf-8">
<title>Crossing the Amber Delta – Workforce Transformation</title>
<link rel="stylesheet" href="https://fonts.googleapis.com/css2?family=Montserrat:wght@400;500;700;800&display=swap">
<style>
  :root {
    --ink: #444547;
    --ink-dark: #1f1f1f;
    --accent-blue: #1f62b8;
    --orange-top: #fb8c00;
    --orange-bottom: #d96d00;
    --band-label: #2b2b2b;
    --white: #ffffff;
  }
  * { margin: 0; padding: 0; box-sizing: border-box; }
  html, body { width: 1200px; height: 528px; overflow: hidden; background: var(--white); }
  .canvas {
    position: relative;
    width: 1200px;
    height: 528px;
    font-family: "Montserrat", Arial, sans-serif;
    color: var(--ink);
  }
  .headline {
    position: absolute;
    top: 26px; left: 0; width: 100%;
    text-align: center;
    font-weight: 800;
    font-size: 37px;
    letter-spacing: 1.5px;
    color: var(--ink);
  }
  .headline-rule {
    position: absolute;
    top: 77px; left: 236px;
    width: 744px; height: 2px;
    background: linear-gradient(90deg, rgba(31,98,184,0), var(--accent-blue) 18%, var(--accent-blue) 82%, rgba(31,98,184,0));
  }
  .diagram { position: absolute; top: 0; left: 0; }
  .band-number { font-family: "Montserrat", Arial, sans-serif; font-size: 17px; font-weight: 500; fill: var(--band-label); }
  .band-label { font-family: "Montserrat", Arial, sans-serif; font-size: 18px; font-weight: 500; fill: var(--band-label); }
  .banner-text { font-family: "Montserrat", Arial, sans-serif; font-size: 21px; font-weight: 800; fill: var(--white); letter-spacing: 0.5px; }
  .method-label {
    position: absolute;
    font-weight: 800;
    font-size: 21px;
    letter-spacing: 1px;
    color: var(--ink-dark);
    text-align: center;
  }
  .method-kanban { left: 66px; top: 346px; width: 160px; }
  .method-kaizen { left: 950px; top: 350px; width: 160px; }
  .method-kokoro { left: 524px; top: 472px; font-size: 20px; text-align: left; }
  .icon { position: absolute; }
  .icon-kanban { left: 90px; top: 251px; }
  .icon-kaizen { left: 985px; top: 247px; }
  .icon-heart { left: 482px; top: 470px; }
</style>
</head>
<body>
<div class="canvas">
  <h1 class="headline">CROSSING THE AMBER DELTA</h1>
  <div class="headline-rule"></div>

  <svg class="diagram" width="1200" height="528" viewBox="0 0 1200 528" aria-label="Workforce transformation pyramid">
    <defs>
      <linearGradient id="banner-fill" x1="0" y1="0" x2="0" y2="1">
        <stop offset="0" stop-color="var(--orange-top)"/>
        <stop offset="1" stop-color="var(--orange-bottom)"/>
      </linearGradient>
      <linearGradient id="band-left" x1="0" y1="0" x2="1" y2="0">
        <stop offset="0" stop-color="#8c8c8c"/>
        <stop offset="1" stop-color="#b4b4b4"/>
      </linearGradient>
      <linearGradient id="band-right-5" x1="0" y1="0" x2="1" y2="0"><stop offset="0" stop-color="#d6d6d6"/><stop offset="1" stop-color="#cfcfcf"/></linearGradient>
      <linearGradient id="band-right-4" x1="0" y1="0" x2="1" y2="0"><stop offset="0" stop-color="#cdcdcd"/><stop offset="1" stop-color="#c2c2c2"/></linearGradient>
      <linearGradient id="band-right-3" x1="0" y1="0" x2="1" y2="0"><stop offset="0" stop-color="#c0c0c0"/><stop offset="1" stop-color="#b3b3b3"/></linearGradient>
      <linearGradient id="band-right-2" x1="0" y1="0" x2="1" y2="0"><stop offset="0" stop-color="#b0b0b0"/><stop offset="1" stop-color="#a2a2a2"/></linearGradient>
      <linearGradient id="band-right-1" x1="0" y1="0" x2="1" y2="0"><stop offset="0" stop-color="#a0a0a0"/><stop offset="1" stop-color="#8e8e8e"/></linearGradient>
      <filter id="banner-shadow" x="-5%" y="-20%" width="110%" height="160%">
        <feDropShadow dx="0" dy="2" stdDeviation="2" flood-color="#000" flood-opacity="0.3"/>
      </filter>
    </defs>

    <!-- banner -->
    <rect x="282" y="150" width="634" height="40" fill="url(#banner-fill)" filter="url(#banner-shadow)"/>
    <text class="banner-text" x="574" y="177" text-anchor="middle">WORKFORCE TRANSFORMATION</text>

    <!-- level bands -->
    <g class="bands">
      <rect x="286" y="214" width="266" height="34" fill="url(#band-left)"/>
      <rect x="552" y="214" width="364" height="34" fill="url(#band-right-5)"/>
      <rect x="286" y="256" width="266" height="34" fill="url(#band-left)"/>
      <rect x="552" y="256" width="364" height="34" fill="url(#band-right-4)"/>
      <rect x="286" y="296" width="266" height="34" fill="url(#band-left)"/>
      <rect x="552" y="296" width="364" height="34" fill="url(#band-right-3)"/>
      <rect x="286" y="336" width="266" height="34" fill="url(#band-left)"/>
      <rect x="552" y="336" width="364" height="34" fill="url(#band-right-2)"/>
      <rect x="286" y="376" width="266" height="34" fill="url(#band-left)"/>
      <rect x="552" y="376" width="364" height="34" fill="url(#band-right-1)"/>
    </g>

    <!-- clearance around the pyramid -->
    <polygon points="552,188 362,420 742,420" fill="var(--white)"/>

    <!-- pyramid tiers -->
    <g class="pyramid">
      <polygon points="552,206 514,264 552,274" fill="#1fb2f2"/>
      <polygon points="552,206 590,264 552,274" fill="#0a8fe2"/>

      <polygon points="522,268 552,276 552,327 480,308" fill="#1a9cf0"/>
      <polygon points="582,268 552,276 552,327 624,308" fill="#0a78e8"/>

      <polygon points="488,312 552,329 552,371 448,344" fill="#167ff0"/>
      <polygon points="616,312 552,329 552,371 656,344" fill="#0868dc"/>

      <polygon points="456,348 552,373 552,412 414,376" fill="#1264d4"/>
      <polygon points="648,348 552,373 552,412 690,376" fill="#0757c4"/>

      <polygon points="422,380 552,414 552,456 384,412" fill="#0d4ca8"/>
      <polygon points="682,380 552,414 552,456 720,412" fill="#074aa8"/>
      <polygon points="384,412 552,456 552,458" fill="#022a66"/>
    </g>

    <!-- band text -->
    <text class="band-number" x="293" y="239">05</text>
    <text class="band-number" x="293" y="280">04</text>
    <text class="band-number" x="293" y="319">03</text>
    <text class="band-number" x="293" y="359">02</text>
    <text class="band-number" x="293" y="399">01</text>
    <text class="band-label" x="764" y="238">Performance</text>
    <text class="band-label" x="766" y="278">Practices</text>
    <text class="band-label" x="766" y="321">Principles</text>
    <text class="band-label" x="766" y="361">People</text>
    <text class="band-label" x="766" y="399">Processes</text>
  </svg>

  <!-- Kanban board icon -->
  <svg class="icon icon-kanban" width="110" height="90" viewBox="0 0 110 90" aria-label="Kanban board icon">
    <rect x="1" y="1" width="108" height="88" rx="6" fill="none" stroke="#8a8a8a" stroke-width="2"/>
    <line x1="6" y1="12" x2="104" y2="12" stroke="#8a8a8a" stroke-width="2"/>
    <line x1="29" y1="6" x2="29" y2="78" stroke="#8a8a8a" stroke-width="2"/>
    <line x1="55" y1="6" x2="55" y2="78" stroke="#8a8a8a" stroke-width="2"/>
    <line x1="81" y1="6" x2="81" y2="78" stroke="#8a8a8a" stroke-width="2"/>
    <rect x="8" y="18" width="17" height="11" fill="#a600ff"/>
    <rect x="8" y="32" width="17" height="11" fill="#0a5dc2"/>
    <rect x="8" y="46" width="17" height="11" fill="#f08000"/>
    <rect x="34" y="18" width="17" height="11" fill="#f08000"/>
    <rect x="34" y="32" width="17" height="11" fill="#66b300"/>
    <rect x="34" y="46" width="17" height="11" fill="#0a5dc2"/>
    <rect x="34" y="60" width="17" height="11" fill="#0a5dc2"/>
    <rect x="60" y="18" width="17" height="11" fill="#a600ff"/>
    <rect x="60" y="32" width="17" height="11" fill="#66b300"/>
    <rect x="86" y="18" width="17" height="11" fill="#1a8cff"/>
    <rect x="86" y="32" width="17" height="11" fill="#f08000"/>
    <rect x="86" y="46" width="17" height="11" fill="#66b300"/>
    <rect x="86" y="60" width="17" height="11" fill="#a600ff"/>
  </svg>
  <div class="method-label method-kanban">KANBAN</div>

  <!-- Kaizen cycle icon -->
  <svg class="icon icon-kaizen" width="90" height="90" viewBox="0 0 90 90" aria-label="Continuous improvement cycle icon">
    <defs>
      <marker id="tip-blue" viewBox="0 0 10 10" refX="3" refY="5" markerWidth="2.4" markerHeight="2.4" orient="auto"><path d="M0,0 L10,5 L0,10z" fill="#1f7be0"/></marker>
      <marker id="tip-orange" viewBox="0 0 10 10" refX="3" refY="5" markerWidth="2.4" markerHeight="2.4" orient="auto"><path d="M0,0 L10,5 L0,10z" fill="#ffaa00"/></marker>
      <marker id="tip-magenta" viewBox="0 0 10 10" refX="3" refY="5" markerWidth="2.4" markerHeight="2.4" orient="auto"><path d="M0,0 L10,5 L0,10z" fill="#e0189a"/></marker>
      <marker id="tip-green" viewBox="0 0 10 10" refX="3" refY="5" markerWidth="2.4" markerHeight="2.4" orient="auto"><path d="M0,0 L10,5 L0,10z" fill="#22c61e"/></marker>
    </defs>
    <g fill="none" stroke-width="9">
      <path d="M50.6 13.5 A32 32 0 0 1 74.5 33" stroke="#1f7be0" marker-end="url(#tip-blue)"/>
      <path d="M76.5 50.6 A32 32 0 0 1 57 74.5" stroke="#ffaa00" marker-end="url(#tip-orange)"/>
      <path d="M39.4 76.5 A32 32 0 0 1 15.5 57" stroke="#e0189a" marker-end="url(#tip-magenta)"/>
      <path d="M13.5 39.4 A32 32 0 0 1 33 15.5" stroke="#22c61e" marker-end="url(#tip-green)"/>
    </g>
  </svg>
  <div class="method-label method-kaizen">KAIZEN</div>

  <!-- Kokoro heart -->
  <svg class="icon icon-heart" width="34" height="30" viewBox="0 0 34 30" aria-label="Heart icon">
    <path d="M17 29 C8 21 1 15 1 8.5 C1 4 4.5 1 8.5 1 C12 1 15 3 17 6 C19 3 22 1 25.5 1 C29.5 1 33 4 33 8.5 C33 15 26 21 17 29z" fill="#ee1111"/>
  </svg>
  <div class="method-label method-kokoro">KOKORO</div>
</div>
</body>
</html>
```